Business Report Cover

We need a revamped quarterly report cover to send to our clients. We asset manage commercial and residential properties throughout the the United States. We use a .pdf version of a cover that we've used for years but would like a fresh updated look for 2018. The cover should include our company logo (KVL Holdings) and a photo of the property as well as the Quarter/Year of the report.

Industry/Entity Type

Business

```html
<!DOCTYPE html>
<html lang="en">
<head>
<meta charset="utf-8">
<title>KVL Holdings – Quarterly Operating Report Cover</title>
<link rel="stylesheet" href="https://fonts.googleapis.com/css2?family=Dosis:wght@400;500;700&display=swap">
<style>
  :root {
    --backdrop: #ece9e4;
    --paper: #ffffff;
    --brand-green: #3b8c60;
    --brand-green-rule: #1f7a45;
    --ink: #111111;
    --on-green: #ffffff;
  }
  html, body {
    margin: 0;
    width: 1200px;
    height: 1200px;
    overflow: hidden;
    background: var(--backdrop);
  }
  .cover {
    position: absolute;
    left: 176px;
    top: 0;
    width: 848px;
    height: 1200px;
    display: block;
    font-family: "Dosis", sans-serif;
  }
  .page { fill: var(--paper); }
  .green-block { fill: var(--brand-green); }
  .green-veil { fill: var(--brand-green); opacity: 0.85; }
  .brand-name { fill: var(--ink); font-weight: 700; }
  .year { fill: var(--on-green); font-weight: 500; font-size: 104px; }
  .report-title { fill: var(--ink); font-weight: 500; font-size: 38px; }
  .title-rule { stroke: var(--brand-green-rule); stroke-width: 5; }
  .property-address { fill: var(--on-green); font-weight: 400; font-size: 22px; }
</style>
</head>
<body>
<svg class="cover" viewBox="0 0 965 1365" xmlns="http://www.w3.org/2000/svg">
  <defs>
    <linearGradient id="property-photo-tones" x1="0" y1="0" x2="0" y2="1">
      <stop offset="0" stop-color="#d9dbe0"/>
      <stop offset="0.35" stop-color="#b9bcc2"/>
      <stop offset="0.55" stop-color="#7a4a3e"/>
      <stop offset="0.75" stop-color="#4a4a4e"/>
      <stop offset="1" stop-color="#3a2a2e"/>
    </linearGradient>
  </defs>

  <rect class="page" x="0" y="0" width="965" height="1365"/>

  <!-- Brand mark -->
  <g class="brand">
    <text class="brand-name" x="65" y="147" font-size="96">KVL</text>
    <text class="brand-name" x="67" y="178" font-size="24" letter-spacing="6">HOLDINGS</text>
  </g>

  <!-- Top-right colour block -->
  <rect class="green-block" x="582" y="0" width="383" height="240"/>

  <!-- Property photograph area -->
  <polygon role="img" aria-label="Photo of the managed property: convenience store with fuel canopy and pumps"
           points="0,303 965,253 965,905 0,970" fill="url(#property-photo-tones)"/>

  <!-- Overlay on photo, top right -->
  <rect class="green-veil" x="582" y="238" width="383" height="115"/>

  <!-- Bottom-left colour block -->
  <polygon class="green-veil" points="0,875 385,848 385,970 0,970"/>
  <polygon class="green-block" points="0,970 385,920 385,1365 0,1365"/>

  <text class="year" x="74" y="1108">2018</text>

  <g class="report-heading">
    <text class="report-title" x="923" y="1052" text-anchor="end">QUARTERLY OPERATING REPORT</text>
    <line class="title-rule" x1="427" y1="1068" x2="965" y2="1068"/>
    <text class="report-title" x="915" y="1112" text-anchor="end" font-size="36">1ST QUARTER</text>
  </g>

  <g class="property-address">
    <text x="83" y="1257">Riverside Corner Market</text>
    <text x="83" y="1288">4170 NE Orchard Grove Ave.</text>
    <text x="83" y="1319">Lakeview, WA 98000</text>
  </g>
</svg>
</body>
</html>
```